Tech Company requires UI design for mobile app

We need a mobile app design for a company based in Singapore called "Valdor Systems". We develop innovative Android/iOS business applications. KelmaRun - a collaboration tool targeted at SMEs that improves reporting and communication between different departments of an organisation. We would like to see designs that use the colour orange, our corporate colour. The final design should communicate clean and technology inclined design.

You are expected to recreate the icons, layout and structure without affecting the workflow.This is a workplace app for employee on mobile. The mobile app aims to empower individual employee to complete the following processes:

1. HR processes - taking attendance, timesheet, employment management to payslip)
2. Inventory management - stock taking, gift redemption and real-time stock management
3. Digital form - application for inspection, safety, procurement or request creation)
4. Job - an app that allows web portal to assign work to individual worker.
Updates

Project Deadline Extended
Reason: Received feedback to extens timeline. Cheers!

Target Market(s)

C-Executive, office employee, retail promoter, worker

Industry/Entity Type

Business

Colors

Designer to choose colors to be used in the design.

Requirements
Must have
• - Design must be neat, looks professional and perceived to be user-friendly
• - Use colour theme for each category
• - Must complement with KelmaRun logo them (already attached)
• - Have "apple" feel
• - We like the layout reference 1 & reference 2 photo. However, we prefer a better colour theme (Already Attached)
• - Please download the link for the work required
• https://files.quorvex.com/open?id=7Hq2LmPzXr4WtYb9NcKd3VfJsEa
Nice to have
• More info to follow shortly
Should not have
• - Must not be loud, flashy, dull, bored,
• - Design should not clash with Kelma Run Logo
• -

```html
<!DOCTYPE html>
<html lang="en">
<head>
<meta charset="utf-8">
<title>Kelma Run – Mobile Workplace App Screens</title>
<link rel="stylesheet" href="https://fonts.googleapis.com/css2?family=Roboto:wght@300;400;500;700&display=swap">
<style>
:root{
  --orange:#f15a24;
  --orange-top:#f47b2b;
  --orange-bot:#ee4723;
  --navy:#1b2433;
  --navy-2:#222d3f;
  --ink:#2b2b2b;
  --muted:#777;
  --line:#e6e6e6;
  --key:#eeeeee;
  --green:#27a844;
  --red:#e5333b;
  --blue:#1e88e5;
  --bg-1:#2b3442;
  --bg-2:#131a23;
}
*{box-sizing:border-box;margin:0;padding:0}
html,body{width:1150px;height:1200px;overflow:hidden}
body{background:radial-gradient(ellipse at 40% 30%,var(--bg-1),var(--bg-2));font-family:'Roboto',sans-serif;color:var(--ink)}
.stage{position:absolute;left:0;top:0;width:1438px;height:1500px;transform:scale(.8);transform-origin:0 0}
.screen{position:absolute;width:270px;height:481px;background:#fff;overflow:hidden}
.abs{position:absolute}
.status{position:absolute;left:0;top:0;width:100%;height:16px;display:flex;justify-content:space-between;align-items:center;padding:0 7px;font-size:8px;color:#fff}
.status .bat{display:inline-block;width:15px;height:6px;background:#fff;border-radius:1px;vertical-align:middle;margin-left:2px}
.orange-bg{background:linear-gradient(180deg,var(--orange-top),var(--orange-bot))}
/* dashboard */
.dash-head{position:absolute;left:0;top:0;width:100%;height:146px}
.brand-sm{position:absolute;left:12px;top:22px;color:#fff;font-size:13px;font-weight:400;display:flex;align-items:center;gap:4px}
.brand-sm .dot{width:7px;height:7px;border-radius:50%;background:#fff}
.head-icons{position:absolute;right:10px;top:20px;display:flex;gap:14px;color:#fff}
.head-icons svg{width:18px;height:18px}
.avatar{position:absolute;border-radius:50%;border:2px solid #fff;background:radial-gradient(circle at 50% 38%,#8a6a58,#3c2b24 70%)}
.who{position:absolute;left:78px;top:62px;color:#fff}
.who b{display:block;font-size:14px;font-weight:500}
.who span{font-size:12px;font-weight:300}
.tabs{position:absolute;left:14px;top:124px;display:flex;gap:15px;font-size:12px;color:rgba(255,255,255,.75);white-space:nowrap}
.tabs .on{color:#fff;font-weight:500;border-bottom:2px solid #fff;padding-bottom:7px}
.feat{position:absolute;width:115px;text-align:center;font-size:10.5px;color:#555}
.feat svg{display:block;margin:0 auto 10px;width:36px;height:36px;color:#444}
.tabbar{position:absolute;left:0;bottom:0;width:100%;height:36px;display:flex;border-top:1px solid #eee;background:#fff}
.tabbar div{flex:1;text-align:center;font-size:6.5px;color:#555;padding-top:4px}
.tabbar svg{display:block;margin:0 auto 2px;width:18px;height:18px;color:#555}
.tabbar .on,.tabbar .on svg{color:var(--orange)}
.tabbar.dark{background:var(--orange);border:none}
.tabbar.dark div,.tabbar.dark svg{color:rgba(255,255,255,.7)}
.tabbar.dark .on,.tabbar.dark .on svg{color:#fff}
/* sub screens */
.bar{position:absolute;left:0;top:0;width:100%;height:42px}
.bar h1{position:absolute;top:19px;width:100%;text-align:center;color:#fff;font-size:12.5px;font-weight:500}
.bar .back{position:absolute;left:11px;top:19px;width:16px;height:16px;color:#fff}
.pill{position:absolute;border-radius:20px;color:#fff;font-size:11px;font-weight:500;text-align:center}
.row{position:absolute;left:10px;right:10px;display:flex;justify-content:space-between;font-size:11.5px}
/* profile */
.card{position:absolute;left:8px;top:42px;width:256px;height:390px;border-radius:8px;overflow:hidden;background:#fff}
.card .top{position:absolute;left:0;top:0;width:100%;height:216px;background:linear-gradient(160deg,var(--navy-2),var(--navy))}
.card .name{position:absolute;top:108px;width:100%;text-align:center;color:#fff;font-size:14.5px;font-weight:500}
.card .sub{position:absolute;top:128px;width:100%;text-align:center;color:#fff;font-size:11.5px;font-weight:300}
.stats{position:absolute;left:0;top:164px;width:100%;height:52px;display:flex}
.stats div{flex:1;text-align:center;padding-top:7px;font-size:11px;font-weight:500}
.stats small{display:block;font-size:6.5px;letter-spacing:.3px;margin-top:5px;font-weight:400;opacity:.6}
.info{position:absolute;left:0;top:216px;width:100%;height:140px;padding:12px 10px}
.info .grid{display:grid;grid-template-columns:115px 1fr;row-gap:26px}
.info small{display:block;font-size:6.5px;letter-spacing:.3px;opacity:.6;margin-bottom:3px}
.info b{font-size:11.5px;font-weight:500}
/* leave status */
.leave-item{position:absolute;left:0;width:100%;height:90px;border-bottom:1px solid var(--line);padding:15px 12px 0 13px}
.leave-item b{display:block;font-size:11px;font-weight:500}
.leave-item span{font-size:11px;color:#555}
.leave-item .badge{position:absolute;right:11px;top:14px;width:64px;height:20px;border-radius:10px;color:#fff;font-size:7.5px;font-weight:700;line-height:20px;text-align:center}
.leave-item .dates{position:absolute;left:13px;right:11px;top:62px;display:flex;justify-content:space-between;font-size:10px;color:#333;align-items:center}
.leave-item .dates em{font-style:normal;color:#888}
.cal-mini{width:11px;height:11px;color:#999;vertical-align:middle;margin-right:7px}
/* leave balance */
.bal{position:absolute;left:7px;width:256px;height:126px;border:1px solid var(--line);border-radius:6px;overflow:hidden;background:#fff}
.bal h3{font-size:12.5px;font-weight:500;padding:9px 10px 0;height:30px}
.bal .r{display:flex;justify-content:space-between;padding:0 10px;height:31px;align-items:center;font-size:11.5px}
.bal .used{background:#f3f3f3;color:var(--red)}
.bal .balc{color:var(--green);font-size:12.5px}
/* forms */
.form-item{position:absolute;left:0;width:100%;height:90px;border-bottom:1px solid var(--line);padding:16px 14px 0}
.form-item b{display:block;font-size:11px;font-weight:500}
.form-item span{font-size:10.5px;color:#555}
.form-item .meta{position:absolute;left:14px;right:14px;top:61px;display:flex;justify-content:space-between;font-size:9.5px;color:#888}
.form-item .pill{right:12px;top:14px;width:64px;height:19px;line-height:19px;font-size:8px;background:var(--orange)}
.brand-mid{position:absolute;width:100%;top:64px;display:flex;justify-content:center;align-items:center;gap:7px;color:#555;font-size:27px;font-weight:300}
.brand-mid .dot{width:14px;height:14px;border-radius:50%;background:var(--orange)}
.check{position:absolute;left:10px;right:12px;display:flex;align-items:center;font-size:11px;height:20px}
.check i{width:14px;height:14px;border-radius:50%;background:#ccc;margin-right:10px;flex:none;position:relative}
.check i.ok{background:var(--orange)}
.check i::after{content:"";position:absolute;left:4px;top:3px;width:4px;height:6px;border:solid #fff;border-width:0 1.5px 1.5px 0;transform:rotate(45deg)}
.check span{flex:1;line-height:1.3}
.check.or span{color:var(--orange)}
.check svg{width:9px;height:9px;color:var(--orange)}
.select{position:absolute;left:150px;width:110px;height:30px;border:1px solid #ccc;border-radius:3px;font-size:11.5px;font-weight:500;padding:7px 9px}
.select svg{position:absolute;right:8px;top:11px;width:9px;height:9px;color:#555}
/* keypad */
.key-c{position:absolute;width:50px;height:50px;border-radius:50%;background:var(--key);color:var(--orange);font-size:18px;text-align:center;line-height:50px}
.numpad{position:absolute;left:0;top:316px;width:100%;height:165px;display:grid;grid-template-columns:repeat(3,1fr);grid-template-rows:repeat(4,1fr);gap:1px;background:#ccc}
.numpad div{background:#fff;text-align:center;font-size:18px;padding-top:4px;line-height:1}
.numpad small{display:block;font-size:6.5px;letter-spacing:1px;margin-top:2px}
.numpad .g{background:#ddd}
.brand-big{position:absolute;left:1180px;top:1135px;display:flex;align-items:center;gap:14px;color:#fff;font-size:44px;font-weight:300;letter-spacing:1px}
.brand-big .dot{width:30px;height:30px;border-radius:50%;background:var(--orange)}
</style>
</head>
<body>
<svg width="0" height="0" style="position:absolute" aria-hidden="true">
<defs>
<symbol id="i-dash" viewBox="0 0 24 24" fill="none" stroke="currentColor" stroke-width="1.6"><rect x="3" y="3" width="7" height="7"/><rect x="14" y="3" width="7" height="7"/><rect x="3" y="14" width="7" height="7"/><rect x="14" y="14" width="7" height="7"/></symbol>
<symbol id="i-cal" viewBox="0 0 24 24" fill="none" stroke="currentColor" stroke-width="1.5"><rect x="3" y="5" width="18" height="16" rx="2"/><path d="M3 9h18M8 3v4M16 3v4"/><path d="M7 13h1M11.5 13h1M16 13h1M7 17h1M11.5 17h1M16 17h1" stroke-width="2"/></symbol>
<symbol id="i-sync" viewBox="0 0 24 24" fill="none" stroke="currentColor" stroke-width="1.6"><path d="M19 12a7 7 0 0 1-11 5.7M5 12a7 7 0 0 1 11-5.7"/><path d="M16 3v3.5h-3.5M8 21v-3.5h3.5"/></symbol>
<symbol id="i-user" viewBox="0 0 24 24" fill="none" stroke="currentColor" stroke-width="1.6"><circle cx="12" cy="8" r="4.5"/><path d="M3.5 21c1-4.5 4.2-7 8.5-7s7.5 2.5 8.5 7z"/></symbol>
<symbol id="i-bell" viewBox="0 0 24 24" fill="none" stroke="currentColor" stroke-width="1.6"><path d="M6 17l2-7a5 5 0 0 1 9.5 1.5L16 19z" transform="rotate(20 12 12)"/><path d="M9 20a3 3 0 0 0 5 0"/></symbol>
<symbol id="i-gear" viewBox="0 0 24 24" fill="none" stroke="currentColor" stroke-width="1.6"><circle cx="12" cy="12" r="3.5"/><circle cx="12" cy="12" r="8" stroke-dasharray="3.2 2"/><circle cx="12" cy="12" r="6.3"/></symbol>
<symbol id="i-back" viewBox="0 0 24 24" fill="none" stroke="currentColor" stroke-width="1.8"><path d="M9 5L3 11l6 6"/><path d="M3 11h11a6 6 0 0 1 6 6v2"/></symbol>
<symbol id="i-chev" viewBox="0 0 10 10" fill="none" stroke="currentColor" stroke-width="1.5"><path d="M3 1l4 4-4 4"/></symbol>
<symbol id="i-down" viewBox="0 0 10 10" fill="none" stroke="currentColor" stroke-width="1.5"><path d="M1 3l4 4 4-4"/></symbol>
<symbol id="f-att" viewBox="0 0 40 40" fill="none" stroke="currentColor" stroke-width="1.8"><circle cx="18" cy="12" r="7"/><path d="M5 35c0-8 5.5-13 13-13 3.5 0 6.5 1 8.5 3"/><path d="M24 31l3.5 3.5 7-8" stroke="#f15a24"/></symbol>
<symbol id="f-today" viewBox="0 0 40 40" fill="none" stroke="currentColor" stroke-width="1.8"><rect x="6" y="8" width="28" height="26" rx="2"/><path d="M12 5v6M28 5v6"/><path d="M12 18h2M19 18h2M26 18h2M12 25h2M19 25h2M26 25h2" stroke-width="2.5"/></symbol>
<symbol id="f-past" viewBox="0 0 40 40" fill="none" stroke="currentColor" stroke-width="1.8"><path d="M4 12h12l3 3h17v18H4z"/><path d="M4 17h32"/><circle cx="28" cy="30" r="6" fill="#fff" stroke="#f15a24"/><path d="M28 27v3h2.5" stroke="#f15a24"/></symbol>
<symbol id="f-pin" viewBox="0 0 40 40" fill="none" stroke="currentColor" stroke-width="1.8"><path d="M20 32S10 21 10 14a10 10 0 0 1 20 0c0 7-10 18-10 18z"/><circle cx="20" cy="14" r="4" stroke="#f15a24"/><path d="M9 29l-5 7h32l-5-7"/></symbol>
<symbol id="f-gift" viewBox="0 0 40 40" fill="none" stroke="currentColor" stroke-width="1.8"><rect x="6" y="15" width="28" height="7"/><path d="M8 22v13h24V22M20 15v20"/><path d="M20 15c-3-6-10-7-9-2 1 2 9 2 9 2zM20 15c3-6 10-7 9-2-1 2-9 2-9 2z" stroke="#f15a24"/></symbol>
<symbol id="f-eye" viewBox="0 0 40 40" fill="none" stroke="currentColor" stroke-width="1.8"><path d="M4 20c5-7 10-10 16-10s11 3 16 10c-5 7-10 10-16 10S9 27 4 20z"/><circle cx="20" cy="20" r="5" fill="#f15a24" stroke="#f15a24"/></symbol>
<symbol id="f-cam" viewBox="0 0 40 40" fill="none" stroke="currentColor" stroke-width="1.8"><rect x="5" y="11" width="30" height="22" rx="2"/><path d="M14 11l2-4h8l2 4"/><circle cx="20" cy="22" r="6" stroke="#f15a24"/></symbol>
<symbol id="f-mon" viewBox="0 0 40 40" fill="none" stroke="currentColor" stroke-width="1.8"><rect x="4" y="7" width="32" height="21" rx="1"/><path d="M20 28v6M13 34h14"/><path d="M9 22l7-7 5 4 8-8" stroke="#f15a24"/></symbol>
<symbol id="f-clip" viewBox="0 0 40 40" fill="none" stroke="currentColor" stroke-width="1.8"><rect x="9" y="6" width="22" height="29" rx="1"/><rect x="15" y="4" width="10" height="5"/><path d="M14 15h12M14 20h12M14 25h7"/><path d="M23 30l2.5 2.5 5-5" stroke="#f15a24"/></symbol>
<symbol id="f-truck" viewBox="0 0 40 40" fill="none" stroke="currentColor" stroke-width="1.8"><path d="M6 12h19v15H6zM25 17h6l4 5v5H25"/><circle cx="12" cy="29" r="3" fill="#fff"/><circle cx="29" cy="29" r="3" fill="#fff"/><path d="M2 16h7M3 20h6" stroke="#f15a24"/></symbol>
<symbol id="f-bag" viewBox="0 0 40 40" fill="none" stroke="currentColor" stroke-width="1.8"><path d="M7 12h26l-3 22H10z"/><path d="M10 12l2-6h16l2 6"/><path d="M15 18a5 5 0 0 0 10 0" stroke="#f15a24"/></symbol>
<symbol id="f-list" viewBox="0 0 40 40" fill="none" stroke="currentColor" stroke-width="1.8"><path d="M9 5h16l6 6v24H9z"/><path d="M25 5v6h6"/><path d="M14 17h12M14 22h12M14 27h12"/></symbol>
<symbol id="f-calx" viewBox="0 0 40 40" fill="none" stroke="currentColor" stroke-width="1.8"><rect x="5" y="8" width="28" height="24" rx="1"/><path d="M5 14h28M11 5v6M27 5v6"/><path d="M9 22h9M15 19l3 3-3 3"/></symbol>
<symbol id="f-brief" viewBox="0 0 40 40" fill="none" stroke="currentColor" stroke-width="1.8"><rect x="5" y="12" width="30" height="21" rx="1"/><path d="M15 12V7h10v5"/><path d="M5 19h30" stroke="#f15a24"/></symbol>
<symbol id="f-forms" viewBox="0 0 40 40" fill="none" stroke="currentColor" stroke-width="1.8"><path d="M12 9h14l5 5v21H12z"/><path d="M8 5h13M8 5v25"/><path d="M16 18h11M16 23h11M16 28h7"/></symbol>
</defs>
</svg>

<main class="stage">

<!-- ===== Row 1 : dashboards ===== -->
<section class="screen" style="left:14px;top:14px">
  <header class="dash-head orange-bg">
    <div class="status"><span>●●●●</span><span>9:41 AM</span><span>100%<i class="bat"></i></span></div>
    <div class="brand-sm"><i class="dot"></i>Kelma</div>
    <div class="head-icons"><svg><use href="#i-bell"/></svg><svg><use href="#i-gear"/></svg></div>
    <div class="avatar" role="img" aria-label="Employee portrait" style="left:14px;top:52px;width:54px;height:54px"></div>
    <div class="who"><b>Daniel Hartwell</b><span>EM1104</span></div>
    <nav class="tabs"><span class="on">Attendance</span><span>Sales</span><span>Inventory</span><span>Leave</span><span>Workforce Management</span></nav>
  </header>
  <div class="feat" style="left:20px;top:198px"><svg><use href="#f-att"/></svg>Take Attendance</div>
  <div class="feat" style="left:135px;top:198px"><svg><use href="#f-today"/></svg>Today</div>
  <div class="feat" style="left:20px;top:310px"><svg><use href="#f-past"/></svg>Past Records</div>
  <div class="feat" style="left:135px;top:310px"><svg><use href="#f-pin"/></svg>Station</div>
  <nav class="tabbar"><div class="on"><svg><use href="#i-dash"/></svg>Dashboard</div><div><svg><use href="#i-cal"/></svg>Calendar</div><div><svg><use href="#i-sync"/></svg>Sync</div><div><svg><use href="#i-user"/></svg>Profile</div></nav>
</section>

<section class="screen" style="left:299px;top:14px">
  <header class="dash-head orange-bg">
    <div class="status"><span>●●●●</span><span>9:41 AM</span><span>100%<i class="bat"></i></span></div>
    <div class="brand-sm"><i class="dot"></i>Kelma</div>
    <div class="head-icons"><svg><use href="#i-bell"/></svg><svg><use href="#i-gear"/></svg></div>
    <div class="avatar" role="img" aria-label="Employee portrait" style="left:14px;top:52px;width:54px;height:54px"></div>
    <div class="who"><b>Daniel Hartwell</b><span>EM1104</span></div>
    <nav class="tabs"><span>Attendance</span><span class="on">Sales</span><span>Inventory</span><span>Leave</span><span>Workforce Management</span></nav>
  </header>
  <div class="feat" style="left:20px;top:198px"><svg><use href="#f-gift"/></svg>New Redemption</div>
  <div class="feat" style="left:135px;top:198px"><svg><use href="#f-eye"/></svg>View Redemptions</div>
  <div class="feat" style="left:20px;top:310px"><svg><use href="#f-cam"/></svg>Take Photo</div>
  <div class="feat" style="left:135px;top:310px"><svg><use href="#f-mon"/></svg>Sales Summary</div>
  <nav class="tabbar"><div class="on"><svg><use href="#i-dash"/></svg>Dashboard</div><div><svg><use href="#i-cal"/></svg>Calendar</div><div><svg><use href="#i-sync"/></svg>Sync</div><div><svg><use href="#i-user"/></svg>Profile</div></nav>
</section>

<section class="screen" style="left:584px;top:14px">
  <header class="dash-head orange-bg">
    <div class="status"><span>●●●●</span><span>9:41 AM</span><span>100%<i class="bat"></i></span></div>
    <div class="brand-sm"><i class="dot"></i>Kelma</div>
    <div class="head-icons"><svg><use href="#i-bell"/></svg><svg><use href="#i-gear"/></svg></div>
    <div class="avatar" role="img" aria-label="Employee portrait" style="left:14px;top:52px;width:54px;height:54px"></div>
    <div class="who"><b>Daniel Hartwell</b><span>EM1104</span></div>
    <nav class="tabs"><span>Attendance</span><span>Sales</span><span class="on">Inventory</span><span>Leave</span><span>Workforce Management</span></nav>
  </header>
  <div class="feat" style="left:20px;top:198px"><svg><use href="#f-clip"/></svg>Inventory Check</div>
  <div class="feat" style="left:135px;top:198px"><svg><use href="#f-truck"/></svg>Delivery</div>
  <div class="feat" style="left:20px;top:310px"><svg><use href="#f-bag"/></svg>New Stock Take</div>
  <div class="feat" style="left:135px;top:310px"><svg><use href="#f-list"/></svg>Stock Take List</div>
  <nav class="tabbar"><div class="on"><svg><use href="#i-dash"/></svg>Dashboard</div><div><svg><use href="#i-cal"/></svg>Calendar</div><div><svg><use href="#i-sync"/></svg>Sync</div><div><svg><use href="#i-user"/></svg>Profile</div></nav>
</section>

<section class="screen" style="left:869px;top:14px">
  <header class="dash-head orange-bg">
    <div class="status"><span>●●●●</span><span>9:41 AM</span><span>100%<i class="bat"></i></span></div>
    <div class="brand-sm"><i class="dot"></i>Kelma</div>
    <div class="head-icons"><svg><use href="#i-bell"/></svg><svg><use href="#i-gear"/></svg></div>
    <div class="avatar" role="img" aria-label="Employee portrait" style="left:14px;top:52px;width:54px;height:54px"></div>
    <div class="who"><b>Daniel Hartwell</b><span>EM1104</span></div>
    <nav class="tabs"><span>Attendance</span><span>Sales</span><span>Inventory</span><span class="on">Leave</span><span>Workforce Management</span></nav>
  </header>
  <div class="feat" style="left:20px;top:198px"><svg><use href="#f-calx"/></svg>Apply Leave</div>
  <div class="feat" style="left:135px;top:198px"><svg><use href="#f-calx"/></svg>Leave Status</div>
  <div class="feat" style="left:20px;top:310px"><svg><use href="#f-today"/></svg>Balance</div>
  <div class="feat" style="left:135px;top:310px"><svg><use href="#f-calx"/></svg>Pending Action</div>
  <nav class="tabbar"><div class="on"><svg><use href="#i-dash"/></svg>Dashboard</div><div><svg><use href="#i-cal"/></svg>Calendar</div><div><svg><use href="#i-sync"/></svg>Sync</div><div><svg><use href="#i-user"/></svg>Profile</div></nav>
</section>

<section class="screen" style="left:1154px;top:14px">
  <header class="dash-head orange-bg">
    <div class="status"><span>●●●●</span><span>9:41 AM</span><span>100%<i class="bat"></i></span></div>
    <div class="brand-sm"><i class="dot"></i>Kelma</div>
    <div class="head-icons"><svg><use href="#i-bell"/></svg><svg><use href="#i-gear"/></svg></div>
    <div class="avatar" role="img" aria-label="Employee portrait" style="left:14px;top:52px;width:54px;height:54px"></div>
    <div class="who"><b>Daniel Hartwell</b><span>EM1104</span></div>
    <nav class="tabs" style="left:-6px"><span>nventory</span><span>Leave</span><span class="on">Workforce Management</span></nav>
  </header>
  <div class="feat" style="left:20px;top:198px;font-size:12px"><svg><use href="#f-forms"/></svg>Forms</div>
  <div class="feat" style="left:135px;top:198px"><svg><use href="#f-brief"/></svg>My Job</div>
  <nav class="tabbar"><div class="on"><svg><use href="#i-dash"/></svg>Dashboard</div><div><svg><use href="#i-cal"/></svg>Calendar</div><div><svg><use href="#i-sync"/></svg>Sync</div><div><svg><use href="#i-user"/></svg>Profile</div></nav>
</section>

<!-- ===== Row 2 ===== -->
<section class="screen" style="left:14px;top:509px">
  <header class="bar orange-bg"><div class="status"><span>●●●●</span><span>9:41 AM</span><span>100%<i class="bat"></i></span></div><svg class="back"><use href="#i-back"/></svg><h1>Attendance</h1></header>
  <div class="avatar" role="img" aria-label="Employee portrait" style="left:10px;top:56px;width:66px;height:66px;border:none"></div>
  <div class="abs" style="left:92px;top:70px;font-size:12px">17 Oct 2017</div>
  <svg class="abs" style="left:116px;top:92px;width:14px;height:14px;color:#999"><use href="#i-cal"/></svg>
  <div class="abs" style="left:196px;top:70px;font-size:12px">10:24 AM</div>
  <svg class="abs" style="left:214px;top:92px;width:14px;height:14px;color:#999" viewBox="0 0 24 24" fill="none" stroke="currentColor" stroke-width="1.6"><circle cx="12" cy="12" r="9"/><path d="M12 7v5l3 2"/></svg>
  <svg class="abs" style="left:10px;top:142px;width:16px;height:12px;color:#888" viewBox="0 0 16 12" fill="none" stroke="currentColor" stroke-width="1.2"><rect x="1" y="1" width="14" height="10" rx="1"/><path d="M4 5h4M4 8h6"/></svg>
  <div class="abs" style="left:36px;top:138px;font-size:13.5px">Daniel Hartwell, EM1104 <span style="display:inline-block;width:10px;height:10px;border-radius:50%;background:var(--green);vertical-align:middle"></span></div>
  <svg class="abs" style="left:11px;top:168px;width:14px;height:16px;color:#888" viewBox="0 0 14 16" fill="none" stroke="currentColor" stroke-width="1.3"><path d="M7 15S2 9 2 6a5 5 0 0 1 10 0c0 3-5 9-5 9z"/><circle cx="7" cy="6" r="2"/></svg>
  <div class="abs" style="left:36px;top:170px;font-size:12px">Larkspur Road</div>
  <div class="abs" role="img" aria-label="Street map around the station location" style="left:0;top:194px;width:270px;height:126px;background:linear-gradient(160deg,#e3e3e3 0%,#d6d6d6 45%,#a9c4dd 70%,#e0e0e0 100%)"></div>
  <svg class="abs" style="left:128px;top:258px;width:12px;height:16px" viewBox="0 0 12 16"><path d="M6 16S0 9 0 6a6 6 0 0 1 12 0c0 3-6 10-6 10z" fill="#e5333b"/><circle cx="6" cy="6" r="2" fill="#fff"/></svg>
  <div class="row" style="top:339px"><span>Project</span><span style="color:#333">KPL-Office 225 <span style="color:#aaa">›</span></span></div>
  <div class="row" style="top:368px"><span>Last Action</span><span style="color:#555">Clock in 16 Oct 2017</span></div>
  <div class="pill" style="left:14px;top:434px;width:87px;height:32px;line-height:32px;background:var(--red)">OUT</div>
  <div class="pill" style="left:169px;top:434px;width:87px;height:32px;line-height:32px;background:var(--green)">IN</div>
</section>

<section class="screen" style="left:299px;top:509px">
  <header class="abs orange-bg" style="left:0;top:0;width:270px;height:112px">
    <div class="status"><span>●●●●</span><span>9:41 AM</span><span>100%<i class="bat"></i></span></div>
    <svg class="abs" style="left:11px;top:19px;width:16px;height:16px;color:#fff"><use href="#i-back"/></svg>
    <div class="abs" style="top:24px;width:100%;text-align:center;color:#fff;font-size:12.5px;font-weight:500">Station</div>
    <div class="pill" style="right:7px;top:20px;width:50px;height:22px;line-height:22px;background:#fff;color:var(--orange);font-size:10px">NEXT</div>
    <div class="abs" style="top:58px;width:100%;text-align:center;color:#fff;font-size:32px;font-weight:400;letter-spacing:1px">EM115</div>
    <div class="abs" style="left:63px;top:98px;width:144px;height:1px;background:rgba(255,255,255,.6)"></div>
  </header>
  <div class="key-c" style="left:22px;top:126px">E</div><div class="key-c" style="left:110px;top:126px">H</div><div class="key-c" style="left:198px;top:126px">J</div>
  <div class="key-c" style="left:22px;top:191px">K</div><div class="key-c" style="left:110px;top:191px">T</div><div class="key-c" style="left:198px;top:191px">Y</div>
  <div class="key-c" style="left:22px;top:256px">A</div><div class="key-c" style="left:110px;top:256px">C</div><div class="key-c" style="left:198px;top:256px">Z</div>
  <div class="numpad">
    <div>1</div><div>2<small>ABC</small></div><div>3<small>DEF</small></div>
    <div>4<small>GHI</small></div><div>5<small>JKL</small></div><div>6<small>MNO</small></div>
    <div>7<small>PQRS</small></div><div>8<small>TUV</small></div><div>9<small>WXYZ</small></div>
    <div class="g" style="font-size:14px;padding-top:12px">+ ✱ #</div><div style="padding-top:10px">0</div><div class="g" style="font-size:13px;padding-top:12px">⌫</div>
  </div>
</section>

<section class="screen orange-bg" style="left:584px;top:509px">
  <header class="bar"><div class="status"><span>●●●●</span><span>9:41 AM</span><span>100%<i class="bat"></i></span></div><svg class="back"><use href="#i-back"/></svg><h1>Profile</h1></header>
  <div class="card">
    <div class="top"></div>
    <div class="avatar" role="img" aria-label="Employee portrait" style="left:94px;top:21px;width:68px;height:68px"></div>
    <div class="name">Daniel Hartwell</div><div class="sub">Male 31</div>
    <div class="stats" style="color:#fff"><div>13 MAY 1986<small>DATE OF BIRTH</small></div><div style="border-left:1px solid rgba(255,255,255,.25);border-right:1px solid rgba(255,255,255,.25)">EM1104<small>EMPLOYEE ID</small></div><div>28 JUL 2015<small>DATE JOINED</small></div></div>
    <div class="info" style="background:#f2f2f2;color:#222"><div class="grid"><div><small>DEPARTMENT</small><b>CONSTRUCTION</b></div><div><small>JOB TITLE</small><b>RIGGER SIGNALMAN</b></div><div><small>CONTACT NUMBER</small><b>90417256</b></div><div><small>SUPERIOR</small><b>MARCUS FENN</b></div></div></div>
    <div class="abs" style="left:0;top:356px;width:100%;height:6px;background:var(--navy)"></div>
  </div>
  <nav class="tabbar dark"><div><svg><use href="#i-dash"/></svg>Dashboard</div><div><svg><use href="#i-cal"/></svg>Calendar</div><div><svg><use href="#i-sync"/></svg>Sync</div><div class="on"><svg><use href="#i-user"/></svg>Profile</div></nav>
</section>

<section class="screen orange-bg" style="left:869px;top:509px">
  <header class="bar"><div class="status"><span>●●●●</span><span>9:41 AM</span><span>100%<i class="bat"></i></span></div><svg class="back"><use href="#i-back"/></svg><h1>Profile</h1></header>
  <div class="card" style="background:var(--navy)">
    <div class="top"></div>
    <div class="avatar" role="img" aria-label="Employee portrait" style="left:94px;top:21px;width:68px;height:68px;border-color:var(--orange)"></div>
    <div class="name">Daniel Hartwell</div><div class="sub">Male 31</div>
    <div class="stats" style="background:#fff;color:#222"><div>13 MAY 1986<small>DATE OF BIRTH</small></div><div>EM1104<small>EMPLOYEE ID</small></div><div>28 JUL 2015<small>DATE JOINED</small></div></div>
    <div class="info" style="color:#fff"><div class="grid"><div><small>DEPARTMENT</small><b>CONSTRUCTION</b></div><div><small>JOB TITLE</small><b>RIGGER SIGNALMAN</b></div><div><small>CONTACT NUMBER</small><b>90417256</b></div><div><small>SUPERIOR</small><b>MARCUS FENN</b></div></div></div>
    <div class="abs" style="left:0;top:356px;width:100%;height:6px;background:var(--orange)"></div>
  </div>
  <nav class="tabbar dark"><div><svg><use href="#i-dash"/></svg>Dashboard</div><div><svg><use href="#i-cal"/></svg>Calendar</div><div><svg><use href="#i-sync"/></svg>Sync</div><div class="on"><svg><use href="#i-user"/></svg>Profile</div></nav>
</section>

<section class="screen" style="left:1154px;top:509px">
  <header class="bar orange-bg"><div class="status"><span>●●●●</span><span>9:41 AM</span><span>100%<i class="bat"></i></span></div><svg class="back"><use href="#i-back"/></svg><h1>Leave Status</h1></header>
  <article class="leave-item" style="top:47px"><b>Daniel Hartwell</b><span>Annual Leave</span><i class="badge" style="background:var(--blue)">PENDING</i><div class="dates"><span><svg class="cal-mini"><use href="#i-cal"/></svg>30 Aug 2017 &nbsp;-&nbsp; 29 Sep 2017</span><em>3 DAYS</em></div></article>
  <article class="leave-item" style="top:137px"><b>Daniel Hartwell</b><span>Sick Leave</span><i class="badge" style="background:var(--green)">APPROVED</i><div class="dates"><span><svg class="cal-mini"><use href="#i-cal"/></svg>31 Jul 2017 &nbsp;-&nbsp; 1 Aug 2017</span><em>2 DAYS</em></div></article>
  <article class="leave-item" style="top:227px"><b>Daniel Hartwell</b><span>Sick Leave</span><i class="badge" style="background:var(--red)">REJECTED</i><div class="dates"><span><svg class="cal-mini"><use href="#i-cal"/></svg>28 Jun 2017 &nbsp;-&nbsp; 29 Jun 2017</span><em>2 DAYS</em></div></article>
  <nav class="tabbar"><div class="on"><svg><use href="#i-dash"/></svg>Dashboard</div><div><svg><use href="#i-cal"/></svg>Calendar</div><div><svg><use href="#i-sync"/></svg>Sync</div><div><svg><use href="#i-user"/></svg>Profile</div></nav>
</section>

<!-- ===== Row 3 ===== -->
<section class="screen" style="left:14px;top:1004px">
  <header class="bar orange-bg"><div class="status"><span>●●●●</span><span>9:41 AM</span><span>100%<i class="bat"></i></span></div><svg class="back"><use href="#i-back"/></svg><h1>Leave Balance</h1></header>
  <div class="bal" style="top:55px"><h3>Annual Leave</h3><div class="r"><span>Entitlement</span><span>14</span></div><div class="r used"><span>Used</span><span>4</span></div><div class="r balc"><span>Balance</span><span>10</span></div></div>
  <div class="bal" style="top:188px"><h3>Sick Leave</h3><div class="r"><span>Entitlement</span><span>14</span></div><div class="r used"><span>Used</span><span>1</span></div><div class="r balc"><span>Balance</span><span>13</span></div></div>
  <div class="bal" style="top:321px"><h3>Child Care Leave</h3><div class="r"><span>Entitlement</span><span>6</span></div><div class="r used"><span>Used</span><span>0</span></div><div class="r balc"><span>Balance</span><span>6</span></div></div>
  <nav class="tabbar"><div class="on"><svg><use href="#i-dash"/></svg>Dashboard</div><div><svg><use href="#i-cal"/></svg>Calendar</div><div><svg><use href="#i-sync"/></svg>Sync</div><div><svg><use href="#i-user"/></svg>Profile</div></nav>
</section>

<section class="screen" style="left:299px;top:1004px">
  <header class="abs orange-bg" style="left:0;top:0;width:270px;height:72px">
    <div class="status"><span>●●●●</span><span>9:41 AM</span><span>100%<i class="bat"></i></span></div>
    <svg class="abs" style="left:11px;top:19px;width:16px;height:16px;color:#fff"><use href="#i-back"/></svg>
    <div class="abs" style="top:24px;width:100%;text-align:center;color:#fff;font-size:12.5px;font-weight:500">Forms</div>
    <div class="abs" style="left:14px;top:49px;width:100px;text-align:center;color:#fff;font-size:12px;padding-bottom:6px;border-bottom:2px solid #fff">New Form</div>
    <div class="abs" style="left:150px;top:49px;width:100px;text-align:center;color:rgba(255,255,255,.7);font-size:12px">Saved Form</div>
  </header>
  <article class="form-item" style="top:72px"><b>QAS Inspection</b><span>Routine Job</span><i class="pill">START</i><div class="meta"><span>ⓘ &nbsp;Version 1.0</span><span>Updated 12 Jan 2017</span></div></article>
  <article class="form-item" style="top:162px"><b>Fault Reporting</b><span>M &amp; E Work</span><i class="pill">START</i><div class="meta"><span>ⓘ &nbsp;Version 5.0</span><span>Updated 1 Oct 2017</span></div></article>
  <article class="form-item" style="top:252px"><b>Toilet Inspection</b><span>Monthly Task</span><i class="pill">START</i><div class="meta"><span>ⓘ &nbsp;Version 1.0</span><span>Updated 28 Jul 2016</span></div></article>
  <nav class="tabbar"><div class="on"><svg><use href="#i-dash"/></svg>Dashboard</div><div><svg><use href="#i-cal"/></svg>Calendar</div><div><svg><use href="#i-sync"/></svg>Sync</div><div><svg><use href="#i-user"/></svg>Profile</div></nav>
</section>

<section class="screen" style="left:584px;top:1004px">
  <header class="bar orange-bg"><div class="status"><span>●●●●</span><span>9:41 AM</span><span>100%<i class="bat"></i></span></div><svg class="back"><use href="#i-back"/></svg><h1>QAS Inspection</h1></header>
  <div class="brand-mid"><i class="dot"></i>Kelma</div>
  <div class="abs" style="top:124px;width:100%;text-align:center;font-size:11.5px;font-weight:500">QAS Inspection</div>
  <div class="abs" style="top:141px;width:100%;text-align:center;font-size:11px;color:#555">Routine Job</div>
  <div class="abs" style="left:38px;top:173px;font-size:10.5px"><svg class="cal-mini"><use href="#i-cal"/></svg>30 Oct 2017 &nbsp;-&nbsp; 30 Oct 2017</div>
  <div class="abs" style="left:38px;top:194px;width:194px;height:1px;background:var(--line)"></div>
  <div class="abs" style="left:38px;top:203px;font-size:10.5px"><svg class="cal-mini" viewBox="0 0 24 24" fill="none" stroke="currentColor" stroke-width="2"><circle cx="12" cy="12" r="9"/><path d="M12 7v5l3 2"/></svg>6:00 - 7:00 PM &nbsp; | &nbsp; Level 1 Female</div>
  <div class="abs" style="left:14px;top:248px;font-size:11.5px;font-weight:500">Note:</div>
  <div class="abs" style="left:14px;top:271px;width:240px;font-size:11px;line-height:16px;color:#333">1. Valid only when the inspection is done with a MA</div>
  <div class="abs" style="left:14px;top:320px;font-size:11px;color:#333">2. 2 Compulsory Signatures</div>
  <div class="pill" style="left:92px;top:420px;width:86px;height:32px;line-height:32px;background:var(--orange)">START</div>
</section>

<section class="screen" style="left:869px;top:1004px">
  <header class="bar orange-bg"><div class="status"><span>●●●●</span><span>9:41 AM</span><span>100%<i class="bat"></i></span></div><svg class="back"><use href="#i-back"/></svg><h1>QAS Inspection</h1></header>
  <div class="brand-mid"><i class="dot"></i>Kelma</div>
  <div class="abs" style="left:10px;top:126px;font-size:11.5px">Time of Inspection:</div>
  <div class="select" style="top:118px">12:25 AM<svg><use href="#i-down"/></svg></div>
  <div class="abs" style="left:10px;top:162px;font-size:11.5px">Inspector:</div>
  <div class="select" style="left:85px;width:175px;top:154px">HALCYON<svg><use href="#i-down"/></svg></div>
  <div class="check or" style="top:202px"><i class="ok"></i><span>Entrance &amp; Lobby</span><svg><use href="#i-chev"/></svg></div>
  <div class="check or" style="top:240px"><i class="ok"></i><span>Corridor Staircase / Landing Steps<br>Common Areas</span><svg><use href="#i-chev"/></svg></div>
  <div class="check or" style="top:281px"><i class="ok"></i><span>Toilets</span><svg><use href="#i-chev"/></svg></div>
  <div class="check" style="top:313px"><i></i><span>Lift Cars</span><svg><use href="#i-chev"/></svg></div>
  <div class="check" style="top:346px"><i></i><span>External Area</span><svg><use href="#i-chev"/></svg></div>
  <div class="check" style="top:378px"><i></i><span>Overall</span><svg><use href="#i-chev"/></svg></div>
  <div class="check" style="top:411px"><i></i><span>Signature</span><svg><use href="#i-chev"/></svg></div>
  <div class="pill" style="left:92px;top:438px;width:86px;height:32px;line-height:32px;background:var(--orange)">SUBMIT</div>
</section>

<div class="brand-big"><i class="dot"></i>Kelma</div>

</main>
</body>
</html>
```